Meridel Haulage - Website

A clean, not cluttered informative website for our business. We specialize in the transportation of radioactive materials across North America. The site is mostly for information about our company and will not be used to attract business but will be used to attract employee's mainly drivers. Driver's are very hard to find in our area. One of the pages needs to be a job's posting page with an apply now button. Either an application can be filled out there or a resume can be uploaded which ever functionality works better. I would like a website that I can easily edit, ability to change text and photos.

Number of Pages Required

5+ page

Colors

Designer to choose colors to be used in the design.

Requirements
Must have
• Home - About - Services - Jobs - Contact pages
• A way prospective employee's can apply or upload their resume to be emailed to me
• Very clean apperance
Should not have
• I don't want it to be busy

```html
<!DOCTYPE html>
<html lang="en">
<head>
<meta charset="utf-8">
<title>Meridel Haulage</title>
<link href="https://fonts.googleapis.com/css2?family=Open+Sans:wght@400;600;700&family=Source+Sans+3:wght@400;600;700;800&display=swap" rel="stylesheet">
<style>
:root{
  --navy:#22222e;
  --navy-2:#2a2a38;
  --red:#e31e24;
  --light:#f4f4f5;
  --text:#555;
  --muted:#8a8a8a;
  --white:#fff;
}
*{box-sizing:border-box;margin:0;padding:0}
html,body{width:1200px;height:3636px;overflow:hidden}
body{font-family:"Open Sans",sans-serif;color:var(--text);background:#fff;position:relative}
.section{position:absolute;left:0;width:1200px}
h1,h2,h3,h4{font-family:"Source Sans 3",sans-serif}

/* header */
.site-header{top:0;height:73px;background:var(--navy)}
.brand{position:absolute;left:176px;top:18px;display:flex;align-items:center;gap:10px;font-family:"Source Sans 3",sans-serif;font-weight:800;font-size:24px;color:var(--white);letter-spacing:.5px}
.brand .dot{width:14px;height:14px;background:var(--red)}
.nav{position:absolute;left:636px;top:0;display:flex;height:73px;align-items:center}
.nav a{font-family:"Source Sans 3",sans-serif;font-weight:600;font-size:16px;color:var(--white);text-decoration:none;padding:0 10px;height:73px;line-height:73px}
.nav a.active{background:var(--red)}
.search{position:absolute;left:992px;top:27px}

/* hero */
.hero{top:73px;height:503px;background:linear-gradient(180deg,#7c8593 0%,#5f6873 45%,#4a4f58 100%)}
.hero-photo{position:absolute;inset:0}
.hero h1{position:absolute;top:160px;width:100%;text-align:center;color:var(--white);font-size:64px;font-weight:800;letter-spacing:1px}
.hero .sub{position:absolute;top:240px;width:100%;text-align:center;color:var(--white);font-family:"Source Sans 3",sans-serif;font-size:40px}
.btn{display:inline-block;background:var(--red);color:var(--white);font-family:"Source Sans 3",sans-serif;font-weight:700;text-transform:uppercase;font-size:14px;text-align:center;border:none}
.hero .btn{position:absolute;left:503px;top:357px;width:194px;height:48px;line-height:48px}
.slide-arrow{position:absolute;top:222px;width:36px;height:42px;background:rgba(0,0,0,.45)}
.slide-arrow.prev{left:40px}.slide-arrow.next{left:1124px}

/* about */
.about{top:576px;height:569px;background:var(--light)}
.about-map{position:absolute;inset:0;background:radial-gradient(ellipse at 50% 55%,#ebebee 0%,var(--light) 70%)}
.intro-card{position:absolute;left:173px;top:-43px;width:854px;height:237px;background:#fff;box-shadow:0 6px 20px rgba(0,0,0,.18)}
.intro-map{position:absolute;left:21px;top:20px;width:230px;height:176px;background:linear-gradient(135deg,#e9e9ec,#dcdce0);border-radius:4px}
.intro-card h2{position:absolute;left:291px;top:28px;width:540px;color:var(--red);font-size:24px;line-height:30px;font-weight:700}
.intro-card p{position:absolute;left:291px;top:102px;width:520px;font-size:13px;line-height:21px;color:var(--muted)}
.more{font-family:"Source Sans 3",sans-serif;font-weight:700;font-size:13px;color:var(--navy);text-transform:uppercase}
.more span{color:var(--red)}
.intro-card .more{position:absolute;left:291px;top:187px}
.feature{position:absolute;top:282px;width:300px;text-align:center}
.feature .icon{margin:0 auto;width:58px;height:58px}
.feature h3{margin-top:14px;font-size:19px;font-weight:600;color:#222}
.feature p{margin-top:12px;font-size:12px;line-height:19px;color:var(--muted)}
.about .view-more{position:absolute;left:0;width:1200px;top:492px;text-align:center}

/* career */
.career{top:1145px;height:745px;background:var(--navy-2)}
.career-photo{position:absolute;left:0;top:0;width:576px;height:745px;background:linear-gradient(160deg,#6d7178 0%,#3d3f45 50%,#26272c 100%)}
.career-tab{position:absolute;left:576px;top:37px;width:176px;height:60px;background:var(--red);color:#fff;font-family:"Source Sans 3",sans-serif;font-weight:700;font-size:30px;line-height:60px;padding-left:30px}
.career-body{position:absolute;left:609px;top:133px;width:520px;color:#ddd}
.career-body h3{color:var(--red);font-size:22px;line-height:28px;font-weight:700}
.career-body p{font-size:13px;line-height:21px;margin-top:14px}
.career-body ul{list-style:none;margin-top:8px}
.career-body li{font-size:13px;line-height:21px;padding:4px 0 4px 22px;position:relative}
.career-body li::before{content:"";position:absolute;left:2px;top:11px;width:7px;height:7px;border-top:2px solid #fff;border-right:2px solid #fff;transform:rotate(45deg)}
.rule{height:1px;background:#4a4a5a;margin:22px 0}
.career .btn{position:absolute;top:652px;height:45px;line-height:45px}
.btn.apply{left:612px;width:146px}
.btn.upload{left:776px;width:154px}

/* testimonials */
.testimonials{top:1890px;height:504px;background:#fff}
.section-title{position:absolute;width:1200px;text-align:center;font-size:32px;font-weight:600;color:#222}
.testimonials .section-title{top:66px}
.quote-card{position:absolute;left:173px;top:155px;width:854px;height:225px;background:var(--navy);border-radius:4px}
.quote-photo{position:absolute;left:0;top:0;width:200px;height:225px;background:linear-gradient(160deg,#a69a88,#5b5248)}
.quote-card blockquote{position:absolute;left:218px;top:32px;width:608px;color:#eee;font-size:14px;line-height:24px}
.quote-card .name{position:absolute;right:52px;top:135px;text-align:right;color:#fff;font-family:"Source Sans 3",sans-serif;font-weight:700;font-size:18px}
.quote-card .role{position:absolute;right:52px;top:161px;color:var(--red);font-size:11px;font-weight:700;text-transform:uppercase}
.dots{position:absolute;top:418px;left:0;width:1200px;display:flex;justify-content:center;gap:14px}
.dots i{width:11px;height:11px;border-radius:50%;background:#999}
.dots i.on{background:var(--red)}

/* contact */
.contact{top:2394px;height:563px;background:linear-gradient(180deg,#2f3340 0%,#3f4450 55%,#565148 80%,#2c2e33 100%)}
.contact .section-title{top:66px;color:#fff}
.field{position:absolute;left:245px;width:710px;background:rgba(255,255,255,.1);border:1px solid rgba(255,255,255,.55);color:#fff;font-size:13px;padding:8px 12px}
.contact .btn{position:absolute;left:245px;top:445px;width:710px;height:43px;line-height:43px}

/* partners */
.partners{top:2957px;height:261px;background:#fff}
.partners .section-title{top:56px}
.partner-row{position:absolute;top:140px;left:173px;width:854px;display:flex;justify-content:space-between;align-items:center}
.partner{height:50px;background:#d9d9dc;border-radius:4px}

/* footer */
.site-footer{top:3218px;height:372px;background:var(--navy);color:#ccc}
.fcol{position:absolute;top:52px}
.fcol h4{color:#fff;font-size:18px;font-weight:700;padding-bottom:10px;border-bottom:1px solid #444;width:272px}
.fcol .line{display:flex;gap:12px;font-size:13px;line-height:20px;margin-top:18px}
.fcol .line svg{flex:none;margin-top:3px}
.socials{display:flex;gap:16px;margin:22px 0 0 52px}
.socials i{width:14px;height:14px;border-radius:50%;background:#bbb}
.fcol p{font-size:13px;line-height:20px;margin-top:18px}
.news-input{margin-top:20px;width:272px;height:34px;background:#2f2f3c;border:1px solid #444}
.site-footer .btn{width:272px;height:34px;line-height:34px;font-size:13px;margin-top:8px}
.footer-map{width:272px;height:112px;margin-top:18px;background:linear-gradient(135deg,#e2ddd0,#c9d4c4);position:relative}
.bottom-bar{top:3590px;height:46px;background:#1a1a23;color:#888;font-size:12px}
.bottom-bar span{position:absolute;left:173px;top:15px}
.to-top{position:absolute;left:990px;top:12px;width:24px;height:24px;background:var(--red)}
</style>
</head>
<body>

<header class="section site-header">
  <div class="brand"><span class="dot"></span>Meridel Haulage</div>
  <nav class="nav">
    <a class="active">Home</a><a>About</a><a>Services</a><a>Jobs</a><a>Contact Us</a>
  </nav>
  <svg class="search" width="18" height="18" viewBox="0 0 18 18"><circle cx="7.5" cy="7.5" r="5.5" fill="none" stroke="#fff" stroke-width="2.2"/><line x1="11.5" y1="11.5" x2="16" y2="16" stroke="#fff" stroke-width="2.4"/></svg>
</header>

<section class="section hero">
  <div class="hero-photo" role="img" aria-label="Semi truck hauling cylindrical containers on a flatbed trailer"></div>
  <h1>MAKES YOU SMILE</h1>
  <div class="sub">Safe Delivery</div>
  <a class="btn">Get Quote Now</a>
  <div class="slide-arrow prev"><svg width="36" height="42"><path d="M21 14l-7 7 7 7" fill="none" stroke="#fff" stroke-width="2.5"/></svg></div>
  <div class="slide-arrow next"><svg width="36" height="42"><path d="M15 14l7 7-7 7" fill="none" stroke="#fff" stroke-width="2.5"/></svg></div>
</section>

<section class="section about">
  <div class="about-map" role="img" aria-label="Faint world map backdrop"></div>
  <div class="intro-card">
    <div class="intro-map" role="img" aria-label="Map of North America with route markers"></div>
    <h2>We specialize in the transportation of radioactive materials across North America</h2>
    <p>Every load we carry is planned, tracked and handled by trained, licensed crews. We follow strict safety rules on every route so that the cargo, the public and our drivers stay protected.</p>
    <div class="more">Read More <span>›</span></div>
  </div>

  <div class="feature" style="left:162px">
    <svg class="icon" viewBox="0 0 58 58"><circle cx="29" cy="29" r="16" fill="none" stroke="#e31e24" stroke-width="2.5"/><path d="M29 19v10l7 5" fill="none" stroke="#e31e24" stroke-width="2.5"/></svg>
    <h3>Fast Service</h3>
    <p>Our crews move quickly without cutting corners, keeping every shipment on schedule from the first mile to the final drop.</p>
  </div>
  <div class="feature" style="left:465px">
    <svg class="icon" viewBox="0 0 58 58"><rect x="11" y="18" width="24" height="18" fill="none" stroke="#e31e24" stroke-width="2.5"/><path d="M35 24h7l5 6v6H35z" fill="none" stroke="#e31e24" stroke-width="2.5"/><circle cx="19" cy="40" r="3.5" fill="#fff" stroke="#e31e24" stroke-width="2.5"/><circle cx="41" cy="40" r="3.5" fill="#fff" stroke="#e31e24" stroke-width="2.5"/></svg>
    <h3>Safe Delivery</h3>
    <p>Certified equipment, sealed containers and careful routing keep sensitive cargo secure until it reaches its destination.</p>
  </div>
  <div class="feature" style="left:768px">
    <svg class="icon" viewBox="0 0 58 58"><circle cx="29" cy="29" r="16" fill="none" stroke="#e31e24" stroke-width="2.5"/><path d="M22 23c0 8 6 14 14 14l2-4-4-2-2 2c-3-1-5-3-6-6l2-2-2-4z" fill="#e31e24"/></svg>
    <h3>24/7 Support</h3>
    <p>Our dispatch team is on call day and night, ready to answer questions and track each load wherever it travels.</p>
  </div>
  <div class="view-more more">View More <span>›</span></div>
</section>

<section class="section career">
  <div class="career-photo" role="img" aria-label="Truck driver at the wheel inside a cab"></div>
  <div class="career-tab">Career</div>
  <div class="career-body">
    <h3>Opportunities for high performing<br>Professional Driver :-</h3>
    <p>We offer top-rate pay and a great Benefits Package which includes</p>
    <ul>
      <li>100 % paid employee health insurance</li>
      <li>Paid holidays &amp; vacation</li>
      <li>Uniforms are also provided</li>
      <li>Meridel Haulage also provides ongoing training to help you be the best you can be!</li>
    </ul>
    <div class="rule"></div>
    <h3>Applicant Requirements :-</h3>
    <ul>
      <li>Must be at least 25 years or older</li>
      <li>2 years of recent verifiable driving experience</li>
      <li>Must have valid Class A CDL license</li>
      <li>Pass a DOT physical (including fit for duty), road test and pre-employment drug screening</li>
    </ul>
  </div>
  <a class="btn apply">Apply Now</a>
  <a class="btn upload">Upload Resume</a>
</section>

<section class="section testimonials">
  <h2 class="section-title">Testimonials</h2>
  <div class="quote-card">
    <div class="quote-photo" role="img" aria-label="Driver standing beside his truck"></div>
    <blockquote>Nam libero tempore, cum soluta nobis est eligendi optio cumque nihil impedit quo minus id quod maxime placeat facere possimus, omnis voluptas assumenda dolor repellendus et voluptates repudiandae sint et molestiae.</blockquote>
    <div class="name">DALE PORTER</div>
    <div class="role">Driver</div>
  </div>
  <div class="dots"><i></i><i></i><i class="on"></i></div>
</section>

<section class="section contact" role="img" aria-label="Truck on a highway at dusk">
  <h2 class="section-title">Contact Us</h2>
  <div class="field" style="top:166px;height:37px">Name...</div>
  <div class="field" style="top:215px;height:37px">Email...</div>
  <div class="field" style="top:263px;height:161px">Message...</div>
  <a class="btn">Submit</a>
</section>

<section class="section partners">
  <h2 class="section-title">Our Partners</h2>
  <div class="partner-row">
    <div class="partner" style="width:200px"></div>
    <div class="partner" style="width:120px"></div>
    <div class="partner" style="width:160px"></div>
    <div class="partner" style="width:150px"></div>
    <div class="partner" style="width:130px"></div>
  </div>
</section>

<footer class="section site-footer">
  <div class="fcol" style="left:173px">
    <h4>Contact Us</h4>
    <div class="line"><svg width="12" height="14" viewBox="0 0 12 14"><path d="M6 0a5 5 0 0 0-5 5c0 4 5 9 5 9s5-5 5-9a5 5 0 0 0-5-5z" fill="#ccc"/><circle cx="6" cy="5" r="2" fill="#22222e"/></svg><span>48 Fairbank Road, Suite 4<br>Greenfield North</span></div>
    <div class="line"><svg width="12" height="12" viewBox="0 0 12 12"><path d="M2 1l2.5 0 1 3-1.5 1c.7 1.5 1.5 2.3 3 3l1-1.5 3 1V11C6 11 1 6 2 1z" fill="#ccc"/></svg><span>(555) 318-4471</span></div>
    <div class="line"><svg width="13" height="10" viewBox="0 0 13 10"><rect width="13" height="10" fill="#ccc"/><path d="M0 0l6.5 5L13 0" fill="none" stroke="#22222e"/></svg><span>info@meridelhaulage.com</span></div>
    <div class="socials"><i></i><i></i><i></i><i></i></div>
  </div>
  <div class="fcol" style="left:464px">
    <h4>Newsletter</h4>
    <p>Subscribe to our newsletter for latest updates</p>
    <div class="news-input"></div>
    <a class="btn">Subscribe</a>
  </div>
  <div class="fcol" style="left:755px">
    <h4>Locate Us</h4>
    <div class="footer-map" role="img" aria-label="Street map showing the office location">
      <svg style="position:absolute;left:124px;top:34px" width="22" height="30" viewBox="0 0 22 30"><path d="M11 0a10 10 0 0 0-10 10c0 8 10 20 10 20s10-12 10-20A10 10 0 0 0 11 0z" fill="#e31e24"/><circle cx="11" cy="10" r="4" fill="#fff"/></svg>
    </div>
  </div>
</footer>
<div class="section bottom-bar"><span>© Copyright Meridel Haulage | All rights reserved</span><div class="to-top"><svg width="24" height="24"><path d="M7 15l5-5 5 5" fill="none" stroke="#fff" stroke-width="2"/></svg></div></div>

</body>
</html>
```